Talbrix Business Card Design

We need a modern great looking premium business card design that can be customized by person that also displays a contact QR code. It should match our existing branding and website Talbrix.com . We need to be able to upload it to zell for continued customization and use across a good size company.

```html
<!DOCTYPE html>
<html lang="en">
<head>
<meta charset="utf-8">
<title>Talbrix Business Card</title>
<link rel="stylesheet" href="https://fonts.googleapis.com/css2?family=Poppins:wght@300;400;600&display=swap">
<style>
  :root {
    --brand-blue: #4470b7;
    --card-white: #ffffff;
    --qr-tint: #e9eef7;
    --backdrop: #e6e6e6;
    --ink: #1d1d1d;
  }
  * { margin: 0; padding: 0; box-sizing: border-box; }
  html, body {
    width: 1200px; height: 1200px; overflow: hidden;
    background: var(--backdrop);
    font-family: "Poppins", sans-serif;
  }
  .card {
    position: absolute;
    left: 151px;
    width: 897px;
    height: 525px;
    box-shadow: 0 3px 10px rgba(0,0,0,0.18);
    overflow: hidden;
  }
  .card--front { top: 60px; background: var(--card-white); }
  .card--back { top: 607px; background: var(--brand-blue); }

  .front-bands { position: absolute; inset: 0; }

  .brand { position: absolute; display: flex; align-items: center; }
  .brand__square { display: block; }
  .brand__name { font-weight: 600; letter-spacing: 1px; line-height: 1; }

  .card--front .brand { left: 71px; top: 81px; }
  .card--front .brand__square { width: 85px; height: 87px; background: var(--brand-blue); margin-right: 48px; }
  .card--front .brand__name { font-size: 70px; color: var(--brand-blue); }

  .card--back .brand { left: 334px; top: 215px; }
  .card--back .brand__square { width: 89px; height: 92px; background: var(--card-white); margin-right: 48px; }
  .card--back .brand__name { font-size: 80px; color: var(--card-white); }

  .person { position: absolute; left: 72px; top: 320px; }
  .person__name { font-size: 39px; font-weight: 600; color: var(--brand-blue); line-height: 1.15; }
  .person__role { font-size: 19px; font-weight: 400; color: var(--ink); line-height: 1.2; }

  .contact {
    position: absolute; right: 92px; top: 384px;
    list-style: none; color: var(--card-white);
  }
  .contact__item {
    display: flex; align-items: center; justify-content: flex-end;
    font-size: 21px; font-weight: 300; line-height: 29px; letter-spacing: 0.3px;
  }
  .contact__icon { width: 14px; height: 14px; margin-left: 14px; fill: var(--card-white); }

  .contact-qr {
    position: absolute; right: 48px; bottom: 48px;
    width: 104px; height: 104px;
    background: var(--qr-tint);
    border: 8px solid var(--card-white);
    border-radius: 6px;
  }
</style>
</head>
<body>
  <section class="card card--front">
    <svg class="front-bands" width="897" height="525" viewBox="0 0 897 525" aria-hidden="true">
      <polygon points="755,39 897,39 897,230 565,230" fill="var(--brand-blue)"/>
      <polygon points="482,340 897,340 897,525 296,525" fill="var(--brand-blue)"/>
    </svg>

    <div class="brand">
      <span class="brand__square"></span>
      <span class="brand__name">Talbrix</span>
    </div>

    <div class="person">
      <p class="person__name">Marten Solberg</p>
      <p class="person__role">Founder</p>
    </div>

    <ul class="contact">
      <li class="contact__item">033 4170 2900
        <svg class="contact__icon" viewBox="0 0 24 24" aria-hidden="true"><path d="M6.6 10.8a15.1 15.1 0 0 0 6.6 6.6l2.2-2.2c.3-.3.7-.4 1-.2 1.1.4 2.300.6 3.6.6.6 0 1 .4 1 1V20c0 .6-.4 1-1 1C10.6 21 3 13.4 3 4c0-.6.4-1 1-1h3.5c.6 0 1 .4 1 1 0 1.3.2 2.5.6 3.6.1.3 0 .7-.2 1z"/></svg>
      </li>
      <li class="contact__item">info@talbrix.com
        <svg class="contact__icon" viewBox="0 0 24 24" aria-hidden="true"><path d="M3 5h18v14H3z" /><path d="M3 6l9 7 9-7" fill="none" stroke="var(--brand-blue)" stroke-width="2"/></svg>
      </li>
      <li class="contact__item">talbrix.com
        <svg class="contact__icon" viewBox="0 0 24 24" aria-hidden="true"><g fill="none" stroke="#ffffff" stroke-width="1.8"><circle cx="12" cy="12" r="9"/><ellipse cx="12" cy="12" rx="4" ry="9"/><path d="M3 12h18M5 7h14M5 17h14"/></g></svg>
      </li>
    </ul>
  </section>

  <section class="card card--back">
    <div class="brand">
      <span class="brand__square"></span>
      <span class="brand__name">Talbrix</span>
    </div>
    <div class="contact-qr" role="img" aria-label="Contact QR code linking to the cardholder's details"></div>
  </section>
</body>
</html>
```